依頼概要
■ 名刺に記載する情報

表面:会社名/役職/氏名/住所/電話/Fax/携帯番号/Mail

裏面:事業内容
一般建設業、埋立工事一式、産業廃棄物、特別産業廃棄物収集運搬業、
山土・山砂・砕石・残土等運搬、販売、処分

許可内容
一般建設業 三重県知事許可   ●●●●●
産業廃棄物収集運搬業許可    ●●●●●
特別産業廃棄物収集運搬業許可 ●●●●●

■ 名刺デザインへの要望

信頼感、誠実さをイメージしシンプルでかっこいいデザインをお願いします。
グラデーションなどを利用し立体感のあるデザインが希望です。

■ 進め方

弊社の希望するイメージに近い提案を1つ(場合によって複数)選択させて頂きます。希望に近づけるために、修正要望を個別にさせて頂くこともあります。コンペ方式のため、修正後に当選されない場合も、どうかご了承ください。

■ その他/注意点

選択させて頂いた名刺デザインの著作権(財産権)等の扱いはTovrix利用規約に従い、弊社に譲渡をお願いします。フォントや画像素材などを利用する場合は上記利用用途に使用できることを確認し、第三者の知的財産権等に注意して下さい。
■ 選んだ理由

信頼感、誠実さをイメージし、シンプルにレイアウトしていただき大変気に入りました。見やすく爽やかな感じで良かったです。ありがとうございました。

■ 提案者全員のお礼・コメント

たくさんのご提案ありがとうございました。また機会がありましたらよろしくお願いします。

```html
<!DOCTYPE html>
<html lang="ja">
<head>
<meta charset="utf-8">
<title>有限会社川島産業 名刺</title>
<link href="https://fonts.googleapis.com/css2?family=Noto+Sans+JP:wght@300;400;500;700&family=Quicksand:wght@500;700&display=swap" rel="stylesheet">
<style>
  :root {
    --page-bg: #e4e4e4;
    --panel-bg: #f1f1f1;
    --card-white: #ffffff;
    --card-tint: #eef4fa;
    --brand-blue: #2a7bbd;
    --brand-blue-dark: #1f68a6;
    --ink: #333333;
    --ink-soft: #555555;
    --ink-muted: #8a8a8a;
    --slate: #3b5566;
    --back-text: #d6e5f3;
    --white: #ffffff;
  }
  * { margin: 0; padding: 0; box-sizing: border-box; }
  html, body { width: 938px; height: 1200px; overflow: hidden; }
  body {
    background: var(--page-bg);
    font-family: "Noto Sans JP", sans-serif;
    color: var(--ink);
    position: relative;
  }
  .panel {
    position: absolute;
    left: 0;
    width: 938px;
    background: var(--panel-bg);
  }
  .panel--front { top: 0; height: 590px; }
  .panel--back { top: 612px; height: 588px; }
  .card {
    position: absolute;
    left: 28px;
    width: 880px;
    overflow: hidden;
  }
  .card--front {
    top: 31px;
    height: 529px;
    background: linear-gradient(120deg, var(--card-white) 35%, var(--card-tint) 100%);
  }
  .card--back {
    top: 641px;
    height: 527px;
    background: linear-gradient(120deg, var(--brand-blue) 0%, var(--brand-blue-dark) 100%);
    color: var(--white);
  }
  .abs { position: absolute; white-space: nowrap; }

  /* brand block */
  .brand-mark {
    position: absolute;
    border-radius: 50%;
  }
  .brand-name {
    font-family: "Noto Sans JP", sans-serif;
    font-weight: 700;
    letter-spacing: 1px;
    line-height: 1;
  }
  .card--front .brand-mark {
    left: 48px; top: 118px; width: 90px; height: 90px;
    background: var(--brand-blue);
  }
  .card--front .brand-name { left: 162px; top: 139px; font-size: 38px; color: var(--slate); }
  .card--front .brand-sub { left: 166px; top: 186px; font-size: 16px; color: var(--slate); font-weight: 500; }

  /* person */
  .title { left: 544px; top: 122px; font-size: 20px; color: var(--ink-soft); }
  .person-name { left: 544px; top: 148px; font-size: 42px; font-weight: 500; letter-spacing: 2px; line-height: 1.1; }
  .person-roman { left: 546px; top: 199px; font-size: 16px; color: var(--ink-muted); font-family: "Quicksand", sans-serif; word-spacing: 38px; }

  /* contact */
  .contact-icon { left: 494px; width: 30px; height: 30px; }
  .icon-mail { top: 293px; }
  .icon-phone { top: 338px; }
  .contact-mail { left: 536px; top: 288px; font-family: "Quicksand", sans-serif; font-weight: 700; font-size: 25px; color: var(--ink); }
  .contact-phone { left: 533px; top: 328px; font-family: "Quicksand", sans-serif; font-weight: 700; font-size: 40px; color: var(--ink); letter-spacing: 1px; }

  /* company */
  .company { left: 452px; top: 418px; font-size: 20px; font-weight: 500; color: var(--ink); }
  .address { left: 452px; top: 450px; font-size: 17px; color: var(--ink-muted); font-weight: 300; }
  .tel-fax { left: 452px; top: 473px; font-size: 17px; color: var(--ink-muted); font-weight: 300; letter-spacing: 0.5px; }
  .tel-fax span + span { margin-left: 28px; }

  /* back */
  .card--back .brand-mark {
    left: 120px; top: 218px; width: 110px; height: 110px;
    border: 3px solid var(--white);
  }
  .card--back .brand-name { left: 72px; top: 350px; font-size: 32px; color: var(--white); }
  .card--back .brand-sub { left: 114px; top: 390px; font-size: 14px; color: var(--white); font-weight: 500; }

  .section-head { font-size: 26px; font-weight: 700; color: var(--white); left: 317px; }
  .head-business { top: 76px; }
  .head-permit { top: 302px; }
  .line { left: 317px; font-size: 21px; color: var(--back-text); font-weight: 400; letter-spacing: 0.5px; }
  .permit-no { left: 685px; font-size: 21px; color: var(--back-text); letter-spacing: 1px; }
</style>
</head>
<body>
  <div class="panel panel--front"></div>
  <div class="panel panel--back"></div>

  <section class="card card--front" aria-label="名刺 表面">
    <div class="brand-mark" aria-hidden="true"></div>
    <div class="abs brand-name">KAWASHIMA</div>
    <div class="abs brand-sub">有限会社川島産業</div>

    <div class="abs title">代表取締役</div>
    <div class="abs person-name">田中 健一</div>
    <div class="abs person-roman">tanaka kenichi</div>

    <svg class="abs contact-icon icon-mail" viewBox="0 0 30 30" aria-hidden="true">
      <rect x="2" y="5" width="26" height="20" fill="none" stroke="#2a7bbd" stroke-width="3"/>
      <polyline points="3,7 15,17 27,7" fill="none" stroke="#2a7bbd" stroke-width="2.5"/>
    </svg>
    <div class="abs contact-mail">kenichi_t@kawasima-s.jp</div>

    <svg class="abs contact-icon icon-phone" viewBox="0 0 30 30" aria-hidden="true">
      <rect x="1" y="1" width="28" height="28" rx="3" fill="#2a7bbd"/>
      <rect x="6" y="17" width="4" height="8" fill="#fff"/>
      <rect x="13" y="12" width="4" height="13" fill="#fff"/>
      <rect x="20" y="6" width="4" height="19" fill="#fff"/>
    </svg>
    <div class="abs contact-phone">090-000-000</div>

    <div class="abs company">有限会社川島産業</div>
    <div class="abs address">〒510-0000　三重県四日市市○○町○○○1 23</div>
    <div class="abs tel-fax"><span>TEL 059-000-000</span><span>FAX059-000-000</span></div>
  </section>

  <section class="card card--back" aria-label="名刺 裏面">
    <div class="brand-mark" aria-hidden="true"></div>
    <div class="abs brand-name">KAWASHIMA</div>
    <div class="abs brand-sub">有限会社川島産業</div>

    <h2 class="abs section-head head-business">業務内容</h2>
    <p class="abs line" style="top:116px">一般建設業、埋立工事一式、産業廃棄物、</p>
    <p class="abs line" style="top:160px">特別産業廃棄物収集運搬業、</p>
    <p class="abs line" style="top:204px">山土･山砂･砕石･残土等運搬、販売、処分</p>

    <h2 class="abs section-head head-permit">許可内容</h2>
    <p class="abs line" style="top:342px">一般建設業　三重県知事許可</p>
    <p class="abs permit-no" style="top:342px">○○○○○</p>
    <p class="abs line" style="top:385px">産業廃棄物収集運搬業許可</p>
    <p class="abs permit-no" style="top:385px">○○○○○</p>
    <p class="abs line" style="top:428px">特別産業廃棄物収集運搬業許可</p>
    <p class="abs permit-no" style="top:428px">○○○○○</p>
  </section>
</body>
</html>
```